Become a real French Pastry chef with an easy 3 step pastry kit box.

The company is specialized in French pastries and the boxes will be sold online, and retail stores. The goal is for anyone who likes to be creative and crafty to create and bake their own traditional french pastry in 3 easy steps right at home. French pastries can be known to take hours to bake. These boxes allow you to make them very quickly, no hassle and they results taste amazing. All the ingredients are from FRANCE. Everything you need is in the box, All you need is water! The box design desired is elegant, simple, glamorous but yet eye catchy for retail distribution. This is a kit box with pre scaled ingredients to make your own eclairs. Box dimensions are 8x6x2.
Updates

Target Market(s)

Middle Aged, middle to upper class housewives who enjoy cooking and baking

Industry/Entity Type

Bakery

Font styles to use
Decorative
Script

Colors

Designer to choose colors to be used in the design.

Requirements
Must have
• This box will be called "The eclair kit by {logo}, or {logo} presents the Eclair kit.
• Has to have the instructions (attached document)
• "This box contains: 4 éclair shells, powder pouch, icing bag, pipping bag and pipping tip"
• Net weight 245g
• Nutrition label (attached)
Nice to have
• An eclair on it.

```html
<!DOCTYPE html>
<html lang="en">
<head>
<meta charset="utf-8">
<title>The Éclair Kit – Box Lid</title>
<link rel="stylesheet" href="https://fonts.googleapis.com/css2?family=Great+Vibes&family=Cormorant+Garamond:wght@500;600&family=Comfortaa:wght@400&family=Open+Sans:wght@600;700&display=swap">
<style>
  :root {
    --page: #fbf1f2;
    --lid: #ffffff;
    --stripe: #fcf4f6;
    --ink: #2e2a2b;
    --frame: #8a8788;
    --burgundy-dark: #5e0f2c;
    --burgundy: #8c1c46;
    --banner-rim: #d2648f;
    --brand-blue: #3a66c9;
    --flag-blue: #3f7be0;
    --flag-red: #f2161c;
    --wash-pink: rgba(243, 191, 212, .9);
    --wash-lilac: rgba(201, 188, 217, .6);
    --wash-clear: rgba(255, 255, 255, 0);
    --pastry: #c88a45;
    --chocolate: #3c1d12;
    --tower: #d9d6d7;
  }
  * { box-sizing: border-box; margin: 0; padding: 0; }
  html, body { width: 1200px; height: 927px; overflow: hidden; background: var(--page); }
  .canvas { position: relative; width: 1200px; height: 927px; }
  .lid {
    position: absolute; left: 80px; top: 70px; width: 1040px; height: 787px;
    background: repeating-linear-gradient(90deg, var(--lid) 0 6px, var(--stripe) 6px 8px);
    box-shadow: 0 10px 30px rgba(120, 60, 80, .12);
  }
  .frame { position: absolute; inset: 0; }
  .wash {
    position: absolute; left: 240px; top: 100px; width: 580px; height: 360px;
    background: radial-gradient(closest-side, var(--wash-pink) 0%, var(--wash-lilac) 50%, var(--wash-clear) 100%);
  }
  .brand {
    position: absolute; left: 0; right: 0; top: 88px; text-align: center;
    font-family: "Cormorant Garamond", serif; font-weight: 600; font-size: 30px;
    color: var(--brand-blue);
  }
  .brand::before {
    content: ""; display: inline-block; width: 14px; height: 14px; border-radius: 50%;
    background: var(--brand-blue); margin-right: 10px; vertical-align: middle;
  }
  .presents {
    position: absolute; left: 0; right: 0; top: 146px; text-align: center;
    font-family: "Cormorant Garamond", serif; font-weight: 600; font-size: 26px;
    letter-spacing: 2px; color: var(--ink);
  }
  .banner { position: absolute; left: 300px; top: 185px; width: 440px; height: 110px; }
  .banner-title {
    position: absolute; left: 300px; top: 195px; width: 440px; text-align: center;
    font-family: "Great Vibes", cursive; font-size: 66px; color: #fff; line-height: 1.3;
  }
  .origin { position: absolute; left: 120px; top: 200px; width: 170px; }
  .flag { position: relative; height: 50px; }
  .flag-blue, .flag-red { position: absolute; width: 40px; height: 30px; }
  .flag-blue { left: 15px; top: 20px; background: var(--flag-blue); }
  .flag-red { left: 85px; top: 0; background: var(--flag-red); }
  .origin-text {
    font-family: "Comfortaa", sans-serif; font-size: 15px; line-height: 1.3;
    color: var(--ink); text-align: center; margin-top: 6px;
  }
  .tagline {
    position: absolute; left: 0; right: 0; top: 318px; text-align: center;
    font-family: "Cormorant Garamond", serif; font-weight: 500; font-size: 31px;
    letter-spacing: 2px; color: var(--ink);
  }
  .eclair-photo {
    position: absolute; left: 420px; top: 380px; width: 300px; height: 130px; border-radius: 40px;
    background: linear-gradient(180deg, var(--chocolate) 0%, var(--chocolate) 42%, var(--pastry) 58%, #b9773a 100%);
  }
  .tower-drawing {
    position: absolute; left: 820px; top: 290px; width: 100px; height: 190px;
    background: var(--tower); clip-path: polygon(47% 0, 53% 0, 100% 100%, 0 100%);
  }
  .net-weight {
    position: absolute; left: 0; right: 0; top: 560px; text-align: center;
    font-family: "Cormorant Garamond", serif; font-weight: 600; font-size: 20px; color: var(--ink);
  }
  .contents {
    position: absolute; left: 350px; top: 660px; width: 340px; padding: 14px 18px;
    border: 1.5px solid var(--ink); text-align: center;
    font-family: "Open Sans", sans-serif; font-weight: 600; font-size: 13px;
    letter-spacing: 1.5px; line-height: 1.45; text-transform: uppercase; color: #555;
  }
  .contents strong { font-weight: 700; color: #444; }
</style>
</head>
<body>
<main class="canvas">
  <section class="lid">
    <div class="wash" role="img" aria-label="Soft pink and lilac watercolour wash"></div>
    <svg class="frame" width="1040" height="787" viewBox="0 0 1040 787" aria-hidden="true">
      <path d="M120 150 Q110 90 190 95 Q260 60 330 90 Q420 40 520 80 Q620 40 720 85 Q800 55 860 100 Q940 95 930 170 Q990 230 940 290 Q990 360 945 420 Q990 490 930 540 Q930 610 850 600 Q780 650 700 610 Q610 660 520 615 Q430 660 340 615 Q260 650 190 605 Q110 610 115 540 Q60 480 105 420 Q55 350 105 290 Q60 220 120 150 Z" fill="none" stroke="var(--frame)" stroke-width="2"/>
      <path d="M126 156 Q118 98 194 101 Q262 68 332 97 Q420 48 520 87 Q620 48 718 92 Q800 62 856 106 Q934 104 924 174 Q982 232 934 292 Q982 360 938 420 Q982 488 924 536 Q924 602 848 594" fill="none" stroke="var(--frame)" stroke-width="1" opacity=".6"/>
    </svg>
    <div class="brand">Maison Lune Bakery</div>
    <div class="presents">presents</div>
    <svg class="banner" viewBox="0 0 440 110" aria-hidden="true">
      <defs>
        <linearGradient id="bannerFill" x1="0" y1="0" x2="1" y2="0">
          <stop offset="0" stop-color="var(--burgundy-dark)"/>
          <stop offset=".5" stop-color="var(--burgundy)"/>
          <stop offset="1" stop-color="var(--burgundy-dark)"/>
        </linearGradient>
      </defs>
      <ellipse cx="220" cy="55" rx="215" ry="48" fill="url(#bannerFill)" stroke="var(--banner-rim)" stroke-width="5"/>
    </svg>
    <div class="banner-title">the Éclair kit</div>
    <div class="origin">
      <div class="flag"><span class="flag-blue"></span><span class="flag-red"></span></div>
      <p class="origin-text">All the ingredients<br>are from FRANCE</p>
    </div>
    <p class="tagline">Create your own traditional french Éclair</p>
    <div class="eclair-photo" role="img" aria-label="Photo of two chocolate-glazed éclairs, one cut to show the filling"></div>
    <div class="tower-drawing" role="img" aria-label="Line drawing of the Eiffel Tower"></div>
    <p class="net-weight">net/w 245g</p>
    <p class="contents"><strong>Contains:</strong> 4 éclair shells, powder pouch, icing bag, pipping bag &amp; pipping tip</p>
  </section>
</main>
</body>
</html>
```